Book title: Lanternfall: The spark of momentum!

This book is called: Lanternfall: The spark of momentum!

A guide to understanding the most popular types of coaching and how to find the perfect coach for you.
The coaching industry has exploded over the past few years as the demand for them has increased. With so many different types of coaches it can be intimidating and overwhelming to find the perfect one for you. To further complicate matters, you may experience times in your life when you require multiple coaches. {Book Title} aims to quite the noise and assist you in finding the perfect coach for you. In this book, you will learn more about the different types of coaching as well as meet a hand-picked selection of coaches from the most popular coaching niches. Each featured coach has provided an exercise designed to move you powerfully forward. We encourage you to work through each exercise so you may experience firsthand the power of working with these incredible coaches.

We would like a professional and simple design. See examples included. We would like to see blood orange included in the design, please see color pallets included as well.

Target Market(s)

Corporate professionals wanting to explore the various types of coaching industry

Industry/Entity Type

Coaching - Health, business, spiritual

Font styles to use
Serif

Colors
EE7325
F08F49
F5BC92
FAE3D3
FDF4ED

Requirements
Must have
• Please include book title: Lanternfall, Subtitle: The spark of momentum! Name of publishing company: Silver Meadow Publishing, Spaces for 8 author names on the front of the cover- Author Name
Nice to have
• A feminine yet corporate feel.
Should not have
• We don't want it

```html
<!DOCTYPE html>
<html lang="en">
<head>
<meta charset="utf-8">
<title>Lanternfall: The Spark of Momentum! — Cover Wrap</title>
<link rel="stylesheet" href="https://fonts.googleapis.com/css2?family=Oswald:wght@300;400&family=Barlow:wght@400;500&family=Montserrat:wght@400;700&display=swap">
<style>
  :root {
    --blood-orange: #f4500c;
    --orange: #ee7325;
    --orange-soft: #f08f49;
    --peach: #f5bc92;
    --blush: #fae3d3;
    --cream: #fdf4ed;
    --white: #ffffff;
    --page: #ffffff;
  }
  * { box-sizing: border-box; margin: 0; padding: 0; }
  html, body {
    width: 1200px; height: 1200px; overflow: hidden;
    background: var(--page);
  }
  .cover-wrap {
    position: absolute; left: 29px; top: 190px;
    width: 1141px; height: 821px;
    background: var(--blood-orange);
    color: var(--white);
  }
  .panel { position: absolute; top: 0; height: 100%; }
  .back-cover { left: 0; width: 548px; }
  .spine { left: 548px; width: 45px; }
  .front-cover { left: 593px; width: 548px; }

  /* lotus artwork area (kept beneath all text) */
  .lotus-art {
    position: absolute; left: 0; width: 100%;
    top: 370px; height: 290px; z-index: 0;
    background:
      radial-gradient(ellipse 62% 95% at 50% 100%, var(--orange-soft) 0%, rgba(240,143,73,0.85) 35%, rgba(245,188,146,0.35) 70%, rgba(245,188,146,0) 100%),
      linear-gradient(180deg, var(--blood-orange) 0%, var(--orange) 40%, var(--orange-soft) 75%, var(--peach) 100%);
  }
  .lotus-art::after {
    content: ""; position: absolute; left: 50%; bottom: 0;
    width: 100px; height: 48px; margin-left: -50px;
    border-radius: 50px 50px 0 0;
    background: var(--orange);
  }
  .text-layer { position: absolute; z-index: 2; }

  /* back */
  .blurb {
    left: 59px; top: 38px; width: 435px;
    font-family: "Barlow", sans-serif; font-size: 14.2px; line-height: 24px;
    text-align: justify; text-align-last: center;
  }
  .blurb p + p { margin-top: 23px; }
  .blurb .title-inline {
    font-family: "Oswald", sans-serif; font-weight: 300; font-size: 17px; line-height: 1;
  }
  .back-publisher {
    left: 59px; top: 707px;
    font-family: "Barlow", sans-serif; font-weight: 500;
    font-size: 19px; line-height: 23px; letter-spacing: 5px;
    text-transform: uppercase;
  }

  /* spine */
  .spine-text {
    position: absolute; left: 50%; writing-mode: vertical-rl;
    transform: translateX(-50%);
    font-family: "Barlow", sans-serif; font-size: 13px;
    letter-spacing: 4px; text-transform: uppercase; white-space: nowrap;
  }
  .spine-title { top: 42px; }
  .spine-publisher { top: 526px; }

  /* front */
  .front-block { left: 0; width: 100%; text-align: center; }
  .kicker {
    top: 36px;
    font-family: "Oswald", sans-serif; font-weight: 300;
    font-size: 44px; line-height: 48px; text-transform: uppercase;
  }
  .main-title {
    top: 87px;
    font-family: "Oswald", sans-serif; font-weight: 300;
    font-size: 88px; line-height: 100px; text-transform: uppercase;
    letter-spacing: -2px; white-space: nowrap;
  }
  .subtitle {
    top: 312px;
    font-family: "Montserrat", sans-serif; font-weight: 700;
    font-size: 16px; line-height: 21.5px; text-transform: uppercase;
    white-space: nowrap;
  }
  .author-list {
    top: 670px;
    font-family: "Montserrat", sans-serif; font-size: 14.8px; line-height: 23px;
  }
  .author-row { display: flex; justify-content: center; gap: 8px; }
  .author-name { text-transform: uppercase; white-space: nowrap; }
  .author-name::before {
    content: ""; display: inline-block; width: 9px; height: 9px;
    border-radius: 50%; background: var(--white);
    margin-right: 8px; vertical-align: 1px;
  }
  .publisher-strip {
    position: absolute; left: 0; bottom: 0; width: 100%; height: 71px; z-index: 1;
    background: linear-gradient(90deg, var(--peach), var(--orange-soft) 50%, var(--peach));
    display: flex; align-items: center; justify-content: center;
  }
  .front-publisher {
    font-family: "Barlow", sans-serif; font-weight: 500;
    font-size: 19px; letter-spacing: 5.5px; text-transform: uppercase;
    color: var(--cream);
  }
</style>
</head>
<body>
  <div class="cover-wrap">
    <section class="panel back-cover">
      <div class="lotus-art" role="img" aria-label="Line-art lotus flower with layered orange and peach petals"></div>
      <div class="text-layer blurb">
        <p>The coaching industry has exploded over the past few years as the demand for them has increased. With so many different types of coaches it can be intimidating and overwhelming to find the perfect one for you. To further complicate matters, you may experience times in your life when you require multiple coaches.</p>
        <p><span class="title-inline">LANTERNFALL: THE SPARK OF MOMENTUM!</span> aims to quite the noise and assist you in finding the perfect coach for you. In this book, you will learn more about the different types of coaching as well as meet a hand-picked selection of coaches from the most popular coaching niches. Each featured coach has provided an exercise designed to move you powerfully forward. We encourage you to work through each exercise so you may experience firsthand the power of working with these incredible coaches.</p>
      </div>
      <div class="text-layer back-publisher">Silver<br>Meadow<br>Publishing</div>
    </section>

    <section class="panel spine">
      <div class="spine-text spine-title">Lanternfall: The Spark of Momentum!</div>
      <div class="spine-text spine-publisher">Silver Meadow Publishing</div>
    </section>

    <section class="panel front-cover">
      <div class="lotus-art" role="img" aria-label="Line-art lotus flower with layered orange and peach petals"></div>
      <h2 class="text-layer front-block kicker">Lanternfall:</h2>
      <h1 class="text-layer front-block main-title">The Spark<br>of Momentum!</h1>
      <p class="text-layer front-block subtitle">A guide to understanding the most popular<br>types of coaching and how to find<br>the perfect one for you</p>
      <div class="text-layer front-block author-list">
        <div class="author-row"><span class="author-name">Author’s Name</span><span class="author-name">Author’s Name</span><span class="author-name">Author’s Name</span></div>
        <div class="author-row"><span class="author-name">Author’s Name</span><span class="author-name">Author’s Name</span><span class="author-name">Author’s Name</span></div>
        <div class="author-row"><span class="author-name">Author’s Name</span><span class="author-name">Author’s Name</span></div>
      </div>
      <div class="publisher-strip" role="img" aria-label="Faint peach petal line pattern band">
        <span class="front-publisher">Silver Meadow Publishing</span>
      </div>
    </section>
  </div>
</body>
</html>
```